Commercial facility maintenance

I need a card design that helps my salesmen make contact with new clients, our product is facility maintenance and heavy industrial maintenance

```html
<!DOCTYPE html>
<html lang="en">
<head>
<meta charset="utf-8">
<title>Harlow Millworks LLC. – Business Card</title>
<link href="https://fonts.googleapis.com/css2?family=Montserrat:wght@400;500;700;800&display=swap" rel="stylesheet">
<style>
  :root {
    --backdrop: #2e2a28;
    --paper: #ffffff;
    --ink: #3a3b3e;
    --ink-soft: #4a4a4a;
    --brand-red: #a3212b;
    --brand-black: #141414;
    --edge-red: #8e1c24;
  }
  * { box-sizing: border-box; margin: 0; padding: 0; }
  html, body {
    width: 1200px; height: 786px; overflow: hidden;
    background: var(--backdrop);
    font-family: "Montserrat", Arial, sans-serif;
  }
  .canvas {
    position: relative; width: 1200px; height: 786px;
    display: flex; align-items: center; justify-content: center; gap: 30px;
  }
  .card {
    position: relative; width: 525px; height: 300px;
    background: var(--paper); overflow: hidden;
    box-shadow: 0 10px 28px rgba(0,0,0,.45);
  }
  .card--back { border-bottom: 4px solid var(--edge-red); }
  .card__swoosh { position: absolute; left: 0; top: 0; width: 525px; height: 300px; }

  .front-mark {
    position: absolute; right: 34px; top: 36px;
    width: 200px; height: 200px; border-radius: 50%;
    border: 3px solid var(--brand-black);
    display: flex; align-items: center; justify-content: center; text-align: center;
    color: var(--ink); font-weight: 800; font-size: 22px; line-height: 1.15;
    letter-spacing: .5px;
  }

  .contact { position: absolute; left: 30px; bottom: 16px; }
  .contact__name {
    color: var(--brand-red); font-weight: 800; font-size: 25px; letter-spacing: .5px; line-height: 1.2;
  }
  .contact__role {
    color: var(--ink-soft); font-size: 13px; letter-spacing: 1px; margin: 2px 0 12px;
  }
  .contact__list { list-style: none; }
  .contact__item {
    display: flex; align-items: center; gap: 8px;
    color: var(--ink-soft); font-size: 14px; line-height: 1.55;
  }
  .contact__icon { width: 13px; height: 13px; flex: none; }

  .back-mark {
    position: absolute; inset: 0;
    display: flex; align-items: center; justify-content: center; gap: 14px;
  }
  .back-mark__dot {
    width: 62px; height: 62px; border-radius: 50%;
    border: 3px solid var(--ink);
  }
  .back-mark__name {
    color: var(--ink); font-weight: 800; font-size: 30px; letter-spacing: 1px; line-height: 1.1;
  }
</style>
</head>
<body>
<main class="canvas">

  <section class="card card--front" aria-label="Card front">
    <svg class="card__swoosh" viewBox="0 0 525 300" aria-hidden="true">
      <path d="M0 0 H235 Q75 35 0 110 Z" fill="var(--brand-black)"/>
      <path d="M258 0 Q85 45 0 138 V122 Q70 38 240 0 Z" fill="var(--brand-red)"/>
    </svg>

    <div class="front-mark">HARLOW<br>MILLWORKS<br>LLC.</div>

    <div class="contact">
      <h1 class="contact__name">DEAN MARLOWE</h1>
      <p class="contact__role">OWNER</p>
      <ul class="contact__list">
        <li class="contact__item">
          <svg class="contact__icon" viewBox="0 0 16 16" aria-hidden="true"><path d="M3 2 L6 2 L7 5 L5 6.5 Q6.5 9.5 9.5 11 L11 9 L14 10 L14 13 Q14 14 13 14 Q3 13 2 3 Q2 2 3 2 Z" fill="var(--brand-red)"/></svg>
          555-214-0187
        </li>
        <li class="contact__item">
          <svg class="contact__icon" viewBox="0 0 16 16" aria-hidden="true"><rect x="1" y="3" width="14" height="10" fill="var(--brand-red)"/><path d="M1 3 L8 9 L15 3" fill="none" stroke="#fff" stroke-width="1.4"/></svg>
          dmarlowe@mailbox.com
        </li>
        <li class="contact__item">
          <svg class="contact__icon" viewBox="0 0 16 16" aria-hidden="true"><circle cx="8" cy="8" r="7" fill="var(--brand-red)"/><path d="M1 8 H15 M8 1 Q4 8 8 15 M8 1 Q12 8 8 15" fill="none" stroke="#fff" stroke-width="1"/></svg>
          harlowmillworksllc.com
        </li>
      </ul>
    </div>
  </section>

  <section class="card card--back" aria-label="Card back">
    <div class="back-mark">
      <span class="back-mark__dot"></span>
      <span class="back-mark__name">HARLOW<br>MILLWORKS LLC.</span>
    </div>
  </section>

</main>
</body>
</html>
```